Horse-Related Social Media Web Design

Need a social media web design for the world’s largest horse training program, Brindlecott Open Equitation. The site features social media components along with educational material and videos with a free downloadable app for horse owners on-the-go. Although members receive a free 30-day membership, they must choose from three levels of membership when they sign up (similar to kinloreva.com). The original design was based off of glimmerdock.com.

We would like a mash-up of the sign-up page for Chatterlume and Quibbly. The home page will feature an intro video, sign-up field and a tag line and sub text such as:
Ready to Connect?
Connect with your horse, yourself, Brindlecott members and friends you haven’t yet met.

The final design should communicate a hip, trendy site for horse-minded people.

We need the design only, sliced for the website. We will do all coding ourselves.

The current website is www.brindlecottlink.com.

Project Deadline Extended
Reason: We've had multiple designers accept the project, but none have submitted designs.

The deadline of our project has been extended, we have guaranteed it and the budget has been raised to $1,250 US.  

We are looking forward to some excellent submissions!
Thank you.

Please think outside the box. The submissions we've received so far look much like our current site. While we would like a clean, simple look, it should also be trendy and convey that the site is fun without implicitly saying so. We will be tailoring down the text and information on the front page and placing the majority of information inside the information pages in the navigation.

Thank you!

Thank you to everyone who has participated in submitting designs for our contest. 

Target Market(s)

Target market is horse owners and lovers across the world. The company has a very international market with campuses in the UK and Australia and followers literally across the world.

Industry/Entity Type

Training

Requirements
Nice to have
• Please explain why you made certain design choices from a useability perspective when you submit the design.

```html
<!DOCTYPE html>
<html lang="en">
<head>
<meta charset="utf-8">
<title>Brindlecott Member – Ready to Connect?</title>
<link href="https://fonts.googleapis.com/css2?family=Roboto+Condensed:wght@300;400;700&family=Roboto:wght@400;500;700&display=swap" rel="stylesheet">
<style>
:root{
  --page:#e6e7e8;
  --topbar:#b5b5b5;
  --header:#d3d4d5;
  --navy:#12307a;
  --navy-dark:#0a1f5c;
  --sky:#1aa3e8;
  --text:#4a4a4a;
  --muted:#6b6b6b;
  --footer-top:#0b2447;
  --footer-bottom:#174a7e;
  --footer-accent:#4aa8e0;
  --gold:#f6c86a;
}
*{box-sizing:border-box;margin:0;padding:0}
html,body{width:912px;height:1200px;overflow:hidden}
body{position:relative;background:var(--page);font-family:"Roboto",Arial,sans-serif;color:var(--text)}
.abs{position:absolute}
.topbar{left:0;top:0;width:912px;height:34px;background:var(--topbar)}
.topbar-links{right:16px;top:13px;font-size:10px;color:#555}
.topbar-links b{color:#333}
.header{left:0;top:34px;width:912px;height:114px;background:var(--header)}
.badge{left:72px;top:45px;width:100px;height:101px;background:linear-gradient(#1f3d8f,#10276a);border:2px solid #c9cdd6;border-radius:3px;text-align:center;color:#fff}
.badge .offer{margin-top:8px;font-family:"Roboto Condensed",sans-serif;font-weight:700;font-size:13px;color:var(--gold);line-height:1}
.badge .offer small{display:block;font-size:7.5px;color:#fff;margin-top:2px}
.badge .name{margin-top:26px;font-family:"Roboto Condensed",sans-serif;font-size:16px;color:#fff}
.badge .tier{font-family:"Roboto Condensed",sans-serif;font-size:10px;color:var(--gold);letter-spacing:.5px}
.socials{left:740px;top:66px;display:flex;gap:3px}
.socials span{width:22px;height:23px;background:#ececec;border:1px solid #bbb;border-radius:2px}
.nav{left:179px;top:111px;width:694px;height:37px;background:linear-gradient(#dcdcdc,#c4c5c6);border-radius:8px 8px 0 0;display:flex;align-items:center}
.nav a{font-family:"Roboto Condensed",sans-serif;font-size:14px;color:#555;text-decoration:none;position:absolute;top:11px}
.nav a.active{color:#2651a6}
.search{left:713px;top:118px;width:148px;height:22px;background:#fff;border:1px solid #aaa;font-size:10px;color:#888;padding:5px 6px}
.search-btn{left:840px;top:118px;width:22px;height:22px;background:#2c3f8f}
.video-frame{left:46px;top:160px;width:569px;height:314px;background:linear-gradient(#a8a9aa,#8d8e8f);border-radius:3px}
.video{left:58px;top:169px;width:542px;height:273px;background:linear-gradient(160deg,#6d7a4a 0%,#9aa167 35%,#7b3046 55%,#5f6d3c 80%,#86955a 100%)}
.play{left:297px;top:273px;width:64px;height:64px;border-radius:50%;background:#111}
.controls{left:52px;top:442px;width:560px;height:28px}
.pause{left:52px;top:443px;width:40px;height:26px;background:#2a2a2a;border-radius:2px}
.track{left:104px;top:454px;width:434px;height:7px;background:#666;border-radius:2px}
.track-fill{left:104px;top:454px;width:38px;height:7px;background:var(--sky);border-radius:2px}
.time{left:117px;top:443px;font-size:7px;background:#fff;color:#222;padding:0 2px}
.hd{left:570px;top:452px;font-size:9px;font-weight:700;color:#8a8a8a;font-style:italic}
.hero-title{left:658px;top:198px;font-family:"Roboto Condensed",sans-serif;font-weight:400;font-size:38px;color:#4a4a4a}
.hero-list{left:660px;top:253px;list-style:none;font-size:14.5px;color:#555;line-height:21.7px}
.hero-list li::before{content:"";display:inline-block;width:7px;height:7px;border-radius:50%;background:#444;margin-right:9px;vertical-align:2px}
.cta{left:662px;top:356px;width:152px;height:37px;border-radius:19px;background:linear-gradient(#2d4ea8,#0b1f66);border:2px solid #d7dbe5;color:#fff;font-family:"Roboto Condensed",sans-serif;font-weight:700;font-size:18px;text-align:center;line-height:33px}
.dots{left:666px;top:442px;display:flex;gap:4px}
.dots span{width:12px;height:12px;border-radius:50%;background:#e4e4e4;border:1px solid #999}
.dots span.on{background:#2b4fa3;border-color:#1a3577}
.shelf{left:44px;top:489px;width:824px;height:32px;background:radial-gradient(ellipse at 50% 0%,rgba(0,0,0,.45),rgba(0,0,0,0) 70%)}
.connect-title{left:0;top:528px;width:912px;text-align:center;font-family:"Roboto Condensed",sans-serif;font-weight:700;font-size:48px;color:#444}
.connect-sub{left:0;top:586px;width:912px;text-align:center;font-size:12px;line-height:15px;color:#555}
.social-btn{width:179px;height:41px;border-radius:3px;background:#fff;padding:5px;box-shadow:0 1px 2px rgba(0,0,0,.2)}
.social-btn div{height:31px;border-radius:2px;color:#fff;font-size:12.5px;display:flex;align-items:center}
.social-btn i{width:20px;height:20px;background:rgba(255,255,255,.85);margin:0 12px 0 8px;border-radius:2px}
.chat{left:256px;top:640px}
.chat div{background:linear-gradient(#213a8c,#0f2468)}
.quib{left:479px;top:640px}
.quib div{background:linear-gradient(#2bb4f2,#129ee3)}
.field{width:179px;height:33px;background:#fff;border:1px solid #c4c4c4;border-radius:3px;font-size:12.5px;color:#888;padding:9px 10px}
.forgot{font-size:10.5px;color:#666}
.login{width:69px;height:25px;background:linear-gradient(#223d92,#0a1d62);border-radius:2px;color:#fff;font-family:"Roboto Condensed",sans-serif;font-weight:700;font-size:15px;text-align:center;line-height:25px}
.join{left:349px;top:881px;width:216px;height:40px;background:#f1f1f1;border:1px solid #aaa;border-radius:2px;font-size:13.5px;color:#444;text-align:center;line-height:38px}
.footer{left:0;top:982px;width:912px;height:218px;background:linear-gradient(170deg,var(--footer-top),var(--footer-bottom));border-top:3px solid var(--sky)}
.fcol h3{font-size:14px;color:var(--footer-accent);font-weight:500;margin-bottom:3px}
.fcol p{font-size:8.6px;color:#fff;line-height:15px}
.news-title{left:412px;top:1017px;font-size:15px;font-weight:500;color:#fff}
.news-input{left:410px;top:1046px;width:168px;height:24px;background:#fff;border-radius:3px;font-size:8px;color:#777;padding:7px 10px}
.subscribe{left:588px;top:1046px;width:76px;height:24px;background:var(--gold);border-radius:3px;font-size:12px;font-weight:700;color:#1a2a50;text-align:center;line-height:24px}
.fsocials{left:733px;top:1046px;display:flex;gap:3px}
.fsocials span{width:24px;height:23px;background:#d9d9d9;border:1px solid #888;border-radius:2px}
.divider{left:0;top:1125px;width:912px;height:1px;background:rgba(255,255,255,.12)}
.legal{left:90px;top:1143px;font-size:9.2px;color:#fff}
.copy{left:90px;top:1158px;font-size:9.2px;color:#2a9ee0}
</style>
</head>
<body>
<div class="abs topbar"></div>
<div class="abs topbar-links"><b>ENG ▾</b> &nbsp;<b>Login</b> &nbsp;| &nbsp;Register &nbsp;| &nbsp;FAQ</div>
<div class="abs header"></div>

<div class="abs badge">
  <div class="offer">FREE 30 DAY<small>TRIAL MEMBERSHIP!</small></div>
  <div class="name">Brindlecott</div>
  <div class="tier">MEMBER</div>
</div>

<div class="abs socials"><span></span><span></span><span></span><span></span><span></span></div>

<nav class="abs nav">
  <a class="active" style="left:18px">HOME</a>
  <a style="left:81px">FEATURES</a>
  <a style="left:170px">PRICING</a>
  <a style="left:248px">BUZZ</a>
  <a style="left:310px">FAQs</a>
  <a style="left:371px">GIVING BACK</a>
  <a style="left:467px">CONTACT</a>
</nav>
<div class="abs search">Search...</div>
<div class="abs search-btn">
  <svg width="22" height="22" viewBox="0 0 22 22"><circle cx="10" cy="9" r="4.5" fill="none" stroke="#fff" stroke-width="2"/><line x1="12.5" y1="12" x2="16" y2="16.5" stroke="#fff" stroke-width="2.2"/></svg>
</div>

<div class="abs video-frame"></div>
<div class="abs video" role="img" aria-label="Intro video still: two riders standing together in a sunlit paddock"></div>
<div class="abs play"><svg width="64" height="64" viewBox="0 0 64 64"><polygon points="26,19 26,45 46,32" fill="#fff"/></svg></div>
<div class="abs pause"><svg width="40" height="26" viewBox="0 0 40 26"><rect x="15" y="7" width="3.5" height="12" fill="#fff"/><rect x="21.5" y="7" width="3.5" height="12" fill="#fff"/></svg></div>
<div class="abs track"></div>
<div class="abs track-fill"></div>
<div class="abs time">00:14</div>
<div class="abs hd">HD ⤧</div>

<h2 class="abs hero-title">Sed Laoreet</h2>
<ul class="abs hero-list">
  <li>Part Social Network</li>
  <li>Part Personal Trainer</li>
  <li>Part Digital Diary</li>
  <li>Brindlecott Connect is fun!</li>
</ul>
<div class="abs cta">LOREM IPSUN</div>
<div class="abs dots"><span class="on"></span><span></span><span></span><span></span></div>
<div class="abs shelf"></div>

<h1 class="abs connect-title">Ready to Connect?</h1>
<p class="abs connect-sub">Connect with your horse, yourself, Brindlecott members<br>and friends you haven’t yet met.</p>

<div class="abs social-btn chat"><div><i></i>Login with Chatterlume</div></div>
<div class="abs social-btn quib"><div><i></i>Login with Quibbly</div></div>

<div class="abs field" style="left:256px;top:711px">Email Address</div>
<div class="abs field" style="left:479px;top:711px">Email Address</div>
<div class="abs field" style="left:256px;top:761px">Password</div>
<div class="abs field" style="left:479px;top:761px">Password</div>
<div class="abs forgot" style="left:256px;top:817px">Forgot your password?</div>
<div class="abs login" style="left:367px;top:809px">Login</div>
<div class="abs forgot" style="left:478px;top:817px">Forgot your password?</div>
<div class="abs login" style="left:590px;top:809px">Login</div>

<div class="abs join">New to Brindlecott? <b>Join Today!</b></div>

<footer class="abs footer"></footer>
<div class="abs fcol" style="left:90px;top:1015px"><h3>About Us</h3><p>Company Info<br>Our Services<br>Clients<br>Partners</p></div>
<div class="abs fcol" style="left:200px;top:1015px"><h3>Advice</h3><p>Sign up<br>Forums<br>Promotion</p></div>
<div class="abs fcol" style="left:296px;top:1015px"><h3>Join In</h3><p>FAQs<br>Solutions<br>Contacts</p></div>
<div class="abs news-title">Join our Newsletter</div>
<div class="abs news-input">Email Address:</div>
<div class="abs subscribe">Subscribe</div>
<div class="abs fsocials"><span></span><span></span><span></span></div>
<div class="abs divider"></div>
<div class="abs legal">Disclaimer &amp; Terms &amp; Conditions &nbsp;| &nbsp;Privacy Policy &nbsp;| &nbsp;Advertise With Us &nbsp;| &nbsp;Contact Us</div>
<div class="abs copy">Brindlecott &nbsp;© 2012. &nbsp;All Rights Reserved</div>
</body>
</html>
```